Marnick Building Materials letterhead template

Simple but professional letterhead template for business communication.
LOGO/name in upper left, balanced by company contact info on right upper.
Subject description, date...
addressee, cc: and BC: if applicable editable info..

Need extra days to review

```html
<!DOCTYPE html>
<html lang="en">
<head>
<meta charset="utf-8">
<title>Marnick Building Materials – Letterhead</title>
<link rel="stylesheet" href="https://fonts.googleapis.com/css2?family=Open+Sans:wght@400;600;700;800&display=swap">
<style>
  :root {
    --brand-blue: #2a5eac;
    --brand-blue-soft: #3f70b8;
    --ink: #1f1f1f;
    --paper: #ffffff;
  }
  * { box-sizing: border-box; margin: 0; padding: 0; }
  html, body { width: 849px; height: 1200px; overflow: hidden; background: var(--paper); }
  .letterhead {
    position: relative;
    width: 849px;
    height: 1200px;
    font-family: "Open Sans", "Helvetica Neue", Arial, sans-serif;
    color: var(--ink);
    overflow: hidden;
  }
  .brand {
    position: absolute;
    left: 57px;
    top: 43px;
    display: flex;
    align-items: center;
    gap: 10px;
  }
  .brand-mark {
    width: 82px;
    height: 82px;
    background: var(--brand-blue);
  }
  .brand-name {
    font-weight: 800;
    font-size: 21px;
    line-height: 27px;
    letter-spacing: 1.2px;
    text-transform: uppercase;
    color: var(--brand-blue);
  }
  .contact {
    position: absolute;
    right: 71px;
    top: 46px;
    text-align: right;
    font-size: 13.5px;
    line-height: 20px;
    color: var(--brand-blue);
    list-style: none;
  }
  .field {
    position: absolute;
    left: 57px;
    right: 71px;
    display: flex;
    align-items: flex-end;
    font-size: 15px;
    color: var(--brand-blue);
  }
  .field-label { white-space: nowrap; line-height: 18px; }
  .field-line {
    flex: 1;
    height: 0;
    border-bottom: 1.5px solid var(--brand-blue);
    margin-left: 20px;
    margin-bottom: -2px;
  }
  .field-date { top: 177px; }
  .field-addressee { top: 231px; }
  .field-cc { top: 265px; }
  .field-bc { top: 299px; }
  .field-subject { top: 340px; font-weight: 700; }
  .letter-body {
    position: absolute;
    left: 56px;
    top: 427px;
    width: 723px;
    font-size: 15.4px;
    line-height: 19.9px;
  }
  .salutation { font-weight: 700; font-size: 15.4px; margin-bottom: 20px; }
  .letter-body p.copy { text-align: justify; margin-bottom: 20px; }
  .closing { margin-top: 0; }
  .signature-area {
    position: absolute;
    left: 57px;
    top: 982px;
    width: 278px;
    height: 88px;
    background: linear-gradient(90deg, #e9e9e9, #f6f6f6);
    border-radius: 44px;
  }
  .site-illustration {
    position: absolute;
    left: 429px;
    top: 995px;
    width: 420px;
    height: 205px;
    background: linear-gradient(135deg, var(--brand-blue-soft), var(--brand-blue));
  }
</style>
</head>
<body>
<main class="letterhead">
  <header>
    <div class="brand">
      <div class="brand-mark"></div>
      <div class="brand-name">Marnick<br>Building<br>Materials</div>
    </div>
    <ul class="contact">
      <li>Address</li>
      <li>Telephone</li>
      <li>Email</li>
      <li>Website</li>
    </ul>
  </header>

  <section class="fields">
    <div class="field field-date"><span class="field-label">Date:</span><span class="field-line"></span></div>
    <div class="field field-addressee"><span class="field-label">Addressee:</span><span class="field-line"></span></div>
    <div class="field field-cc"><span class="field-label">CC:</span><span class="field-line"></span></div>
    <div class="field field-bc"><span class="field-label">BC:</span><span class="field-line"></span></div>
    <div class="field field-subject"><span class="field-label">Subject:</span><span class="field-line"></span></div>
  </section>

  <article class="letter-body">
    <p class="salutation">Dear Sir / Madam</p>
    <p class="copy">Lorem ipsum dolor sit amet, consectetuer adipiscing elit, sed diam nonummy nibh euismod tincidunt ut laoreet dolore magna aliquam erat volutpat. Ut wisi enim ad minim veniam, quis nostrud exerci tation ullamcorper suscipit lobortis nisl ut aliquip ex ea commodo consequat. Duis autem vel eum iriure dolor in hendrerit in vulputate velit esse molestie consequat, vel illum dolore eu feugiat nulla facilisis at vero eros et accumsan et iusto odio dignissim qui blandit praesent luptatum zzril delenit augue duis dolore te feugait nulla facilisi.<br>suscipit lobortis nisl ut aliquip ex ea commodo consequat.</p>
    <p class="copy">Lorem ipsum dolor sit amet, consectetuer adipiscing elit, sed diam nonummy nibh euismod nostrud exerci tation ullamcorper suscipit lobortis nisl ut aliquip ex ea commodo consequat. Duis autem vel eum iriure dolor in hendrerit in vulputate velit esse molestie consequat, vel blandit praesent luptatum zzril delenit augue duis dolore te feugait nulla facilisi.<br>dolore magna aliquam erat volutpat. Ut wisi enim ad minim veniam, quis nostrud exerci tation ullamcorper suscipit lobortis nisl ut aliquip ex ea commodo consequat.</p>
    <p class="copy">Lorem ipsum dolor sit amet, consectetuer adipiscing elit, sed diam nonummy nibh euismod tincidunt ut laoreet dolore magna aliquam erat volutpat. Ut wisi enim ad minim veniam, quis nostrud exerci tation ullamcorper iusto odio dignissim qui blandit praesent luptatum zzril delenit augue duis dolore te feugait nulla facilisi.</p>
    <p class="copy">Lorem ipsum dolor sit amet, cons ectetuer adipiscing elit, sed diam nonummy nibh euismod tincidunt ut laoreet dolore magna aliquam erat volutpat. Ut wisi enim ad minim veniam, quis nostrud exerci tation ullamcorper suscipit lobortis nisl ut aliquip ex ea commodo consequat.</p>
    <p class="closing">Yours Sinciery,</p>
  </article>

  <div class="signature-area" role="img" aria-label="Handwritten signature"></div>

  <div class="site-illustration" role="img" aria-label="Illustration of a hard hat and trowel resting on a brick wall"></div>
</main>
</body>
</html>
```